Rex Tollbridge (Burn The Stack) CD Cover Design

Professional Cd cover design needed. No photo of the artist necessary for this cover. You can search Rex Tollbridge on YouTube for a feel of the artist, inspiration, etc. Song (Burn The Stack)!

Target Market(s)

Big money makers , Hustlers, those who don't mind spending cash.

Colors

Designer to choose colors to be used in the design.

Requirements
Nice to have
• Any symbols related to money.

```html
<!DOCTYPE html>
<html lang="en">
<head>
<meta charset="utf-8">
<title>Rex Tollbridge — Burn The Stack</title>
<link rel="stylesheet" href="https://fonts.googleapis.com/css2?family=Inter:wght@600&display=swap">
<style>
  :root {
    --ink-white: #ffffff;
    --night: #07161a;
    --ember-pale: #f7b46a;
    --ember: #e0782a;
    --rust: #9a3418;
    --oxblood: #3c0d0c;
    --flare-red: #ff2a14;
    --flare-gold: #fff06a;
  }
  html, body {
    margin: 0;
    padding: 0;
    width: 1200px;
    height: 1200px;
    overflow: hidden;
    background: var(--night);
  }
  .cover {
    position: relative;
    width: 1200px;
    height: 1200px;
    overflow: hidden;
  }
  .cover svg {
    display: block;
  }
  .artist-name,
  .track-title {
    font-family: "Inter", "Helvetica Neue", Arial, sans-serif;
    font-weight: 600;
    fill: var(--ink-white);
  }
  .artist-name {
    font-size: 162px;
    letter-spacing: -0.02em;
  }
  .track-title {
    font-size: 250px;
    letter-spacing: -0.03em;
  }
</style>
</head>
<body>
<div class="cover">
  <svg width="1200" height="1200" viewBox="0 0 1200 1200" xmlns="http://www.w3.org/2000/svg">
    <defs>
      <linearGradient id="burn-glow" x1="0" y1="0" x2="1" y2="0">
        <stop offset="0" stop-color="var(--ember-pale)"/>
        <stop offset="0.12" stop-color="var(--ember)"/>
        <stop offset="0.28" stop-color="#c8561f"/>
        <stop offset="0.38" stop-color="var(--rust)"/>
        <stop offset="0.52" stop-color="#b4471c"/>
        <stop offset="0.62" stop-color="var(--ember)"/>
        <stop offset="0.72" stop-color="var(--rust)"/>
        <stop offset="0.8" stop-color="var(--night)"/>
        <stop offset="1" stop-color="var(--night)"/>
      </linearGradient>
      <linearGradient id="shadow-fall" x1="0" y1="0" x2="0" y2="1">
        <stop offset="0.4" stop-color="var(--oxblood)" stop-opacity="0"/>
        <stop offset="0.75" stop-color="var(--oxblood)" stop-opacity="0.85"/>
        <stop offset="1" stop-color="#10090a" stop-opacity="0.95"/>
      </linearGradient>
      <radialGradient id="flare" cx="0.5" cy="0.5" r="0.5">
        <stop offset="0" stop-color="var(--flare-gold)"/>
        <stop offset="0.45" stop-color="var(--flare-red)"/>
        <stop offset="1" stop-color="var(--flare-red)" stop-opacity="0"/>
      </radialGradient>
      <filter id="soften"><feGaussianBlur stdDeviation="18"/></filter>
    </defs>

    <g class="backdrop" role="img" aria-label="Abstract blurred film photograph of warm orange and red light fading into a dark band">
      <rect width="1200" height="1200" fill="url(#burn-glow)"/>
      <rect x="340" y="0" width="330" height="1200" fill="url(#shadow-fall)" filter="url(#soften)"/>
      <ellipse cx="935" cy="700" rx="55" ry="560" fill="url(#flare)" filter="url(#soften)"/>
    </g>

    <text class="artist-name" transform="translate(132 1172) rotate(-90)"
          textLength="1140" lengthAdjust="spacingAndGlyphs">REX TOLLBRIDGE</text>

    <text class="track-title" transform="translate(1070 14) rotate(90)"
          textLength="1180" lengthAdjust="spacingAndGlyphs">burn the $tack</text>
  </svg>
</div>
</body>
</html>
```